Design for sports training app

We need the design for 9 screens of an app that supports trainers of sport teams in preparing their training sessions. Regarding colors, fonts etc. there is absolute freedom for the designer to choose what he thinks is best.
The app will be called "Vellix", our idea for the logo is something like a stopwatch.
Wireframes are attached for every screen. You don't have to stick to those - if you have better ideas, we are happy to see them.
Our strategy is "mobile first". Based on the app design we will create a homepage later - I guess it makes sense to give this to the same person, let's see.
The deliverables are attached.
All in all the main target is to present a very simple, intuitive and nice UI that the user can work with without much learning.
Updates
Target Market(s)
Soccer trainers
Industry/Entity Type
Training
Look and feel

```html
<!DOCTYPE html>
<html lang="en">
<head>
<meta charset="utf-8">
<title>Vellix – training app screens</title>
<link href="https://fonts.googleapis.com/css2?family=Quicksand:wght@400;500;600;700&display=swap" rel="stylesheet">
<style>
:root{
  --board-a:#d97c72; --board-b:#c4625a;
  --ink-dark:#1c1e20; --bar-dark:#25282b; --status:#1a1c1e;
  --light-a:#e3e3e3; --light-b:#f3f3f3;
  --text:#3a3d40; --muted:#9a9da0; --line:#d4d4d4;
  --coral:#f47c6f; --coral-soft:#f59486;
  --teal:#4fd6b0; --sky:#7fd0ef; --violet:#9c8fcb;
  --field:#7ed59a; --yellow:#f5d33b; --white:#fff;
}
*{box-sizing:border-box;margin:0;padding:0}
html,body{width:1200px;height:1200px;overflow:hidden}
body{font-family:"Quicksand",sans-serif;color:var(--text)}
.board{width:1500px;height:1500px;transform:scale(.8);transform-origin:0 0;position:relative;
  background:linear-gradient(160deg,var(--board-a),var(--board-b))}
.phone{position:absolute;width:280px;height:496px;overflow:hidden;
  background:linear-gradient(180deg,var(--light-a),var(--light-b))}
.phone.dark{background:var(--ink-dark)}
.abs{position:absolute}
.status{position:absolute;top:0;left:0;right:0;height:14px;background:var(--status);color:#cfd1d3;
  font-size:8px;font-weight:500;display:flex;justify-content:space-between;align-items:center;padding:0 7px}
.status .batt{width:16px;height:6px;border:1px solid #cfd1d3;border-radius:1px;position:relative}
.status .batt::after{content:"";position:absolute;left:1px;top:1px;width:6px;height:2px;background:#cfd1d3}
.topbar{position:absolute;top:14px;left:0;right:0;height:38px;background:var(--bar-dark);color:var(--white);
  font-size:11px;font-weight:700;display:flex;align-items:center;justify-content:center;letter-spacing:.2px}
.topbar .back{position:absolute;left:12px;top:13px;width:9px;height:9px;border-left:2px solid #fff;border-bottom:2px solid #fff;transform:rotate(45deg)}
.photo{position:absolute;inset:14px 0 0 0;background:radial-gradient(ellipse at 55% 40%,#3a3d40 0%,#202224 55%,#111213 100%)}
.wordmark{color:var(--white);font-weight:700;letter-spacing:1px}
.muted{color:var(--muted)}
/* login */
.field-line{position:absolute;left:32px;right:32px;height:1px;background:#4a4d50}
.field-label{position:absolute;left:32px;font-size:9px;color:#cfd1d3}
.btn-login{position:absolute;left:46px;width:188px;top:298px;height:36px;background:var(--coral);color:#fff;
  border-radius:3px;font-size:13px;font-weight:700;display:flex;align-items:center;justify-content:center}
/* dashboard */
.hero{position:absolute;top:14px;left:0;right:0;height:150px;background:var(--bar-dark);color:#fff}
.datecard{position:absolute;left:20px;top:80px;width:40px;height:40px;background:#f1ede6;border-radius:3px;overflow:hidden;text-align:center}
.datecard .m{background:var(--coral);color:#fff;font-size:7px;font-weight:700;height:12px;line-height:12px}
.datecard .d{color:#2b2d30;font-size:14px;font-weight:700;line-height:26px}
.wx{position:absolute;right:12px;top:88px;font-size:9px;line-height:13.5px;color:#d4d6d8;display:grid;grid-template-columns:auto auto;column-gap:8px;text-align:right}
.wx span:nth-child(even){text-align:left}
.bigbtn{position:absolute;left:87px;top:186px;width:106px;height:106px;border-radius:50%;
  background:radial-gradient(circle at 45% 35%,#ffffff,#e9e9e9);box-shadow:0 10px 18px rgba(0,0,0,.12)}
.section-title{position:absolute;left:12px;font-size:9px;font-weight:700;color:#2b2d30}
.row{position:absolute;left:0;right:0;height:20px;display:flex;align-items:center;font-size:9.5px}
.row .flag{width:5px;height:16px;margin-right:12px}
.row .name{width:110px}
.pill{height:14px;border-radius:7px;color:#fff;font-size:8.5px;font-weight:700;display:flex;align-items:center;justify-content:center;width:58px}
.chev{position:absolute;right:24px;width:6px;height:6px;border-right:1.4px solid #555;border-top:1.4px solid #555;transform:rotate(45deg)}
.link-row{position:absolute;left:12px;right:12px;height:26px;border-bottom:1px solid var(--line);font-size:9.5px;font-weight:700;display:flex;align-items:center;color:#2b2d30}
.band{position:absolute;left:0;right:0;height:20px;background:#c9c9c9;font-size:11px;font-weight:700;display:flex;align-items:center;justify-content:center;color:#1c1e20}
.para{position:absolute;font-size:8.6px;line-height:10.8px;text-align:justify;color:#4a4d50}
.finish{position:absolute;left:0;right:0;bottom:0;height:40px;background:var(--violet);color:#fff;font-size:11px;font-weight:700;letter-spacing:.6px;display:flex;align-items:center;justify-content:center}
.pitch{position:absolute;background:var(--field)}
/* tab bar */
.tabbar{position:absolute;left:0;right:0;bottom:0;height:42px;background:var(--bar-dark);display:flex}
.tab{flex:1;display:flex;flex-direction:column;align-items:center;justify-content:flex-end;padding-bottom:3px;font-size:7px;color:#5d6165;gap:3px}
.tab.on{color:#fff}
.tab svg{stroke:currentColor;fill:none;stroke-width:1.6}
/* sliders */
.slider-label{position:absolute;left:14px;font-size:8.5px;color:var(--muted)}
.track{position:absolute;left:32px;width:214px;height:4px;border-radius:2px;background:#d2d2d2;box-shadow:inset 0 1px 1px rgba(0,0,0,.08)}
.fill{height:4px;border-radius:2px}
.fill.coral{background:var(--coral-soft)} .fill.teal{background:var(--teal)}
.knob{position:absolute;top:-5px;width:13px;height:13px;margin-left:-6px;border-radius:50%;background:#f7f7f7;box-shadow:0 1px 3px rgba(0,0,0,.3)}
.scale{position:absolute;font-size:7.5px;color:var(--muted)}
/* equipment */
.kit{position:absolute;left:18px;right:18px;height:34px;border-bottom:1px solid var(--line);display:flex;align-items:center;font-size:10px;font-weight:600;color:#2b2d30}
.kit .qty{margin-left:auto;color:var(--muted);font-weight:500;font-size:9px}
.step{width:12px;height:12px;border-radius:50%;background:#e4e4e4;color:#bbb;font-size:6px;display:flex;align-items:center;justify-content:center}
.step.on{background:var(--teal);color:#fff}
.stepper{margin-left:auto;display:flex;align-items:center;gap:12px}
.stepper .qty{margin:0;width:14px;text-align:center}
</style>
</head>
<body>
<main class="board" role="img" aria-label="Nine Vellix app screens on a coral board">

<!-- 1 splash -->
<section class="phone dark" style="left:24px;top:171px">
  <div class="photo" role="img" aria-label="Dim photo of a soccer player kicking a ball"></div>
  <div class="status"><span>●●○○○ Carrierly</span><span>14:39</span><span class="batt"></span></div>
  <div class="abs" style="left:44px;top:234px;display:flex;align-items:center;gap:10px">
    <span style="width:28px;height:28px;border:3px solid #fff;border-radius:50%"></span>
    <span class="wordmark" style="font-size:34px">VELLIX</span>
  </div>
</section>

<!-- 2 login -->
<section class="phone dark" style="left:318px;top:171px">
  <div class="photo" role="img" aria-label="Dim photo of a soccer player kicking a ball"></div>
  <div class="status"><span>●●○○○ Carrierly</span><span>14:39</span><span class="batt"></span></div>
  <div class="wordmark abs" style="left:0;right:0;top:112px;text-align:center;font-size:18px">VELLIX</div>
  <p class="abs" style="left:20px;right:20px;top:146px;text-align:center;font-size:7.4px;font-weight:700;color:#fff;line-height:9.5px">The inspire success formula is an intense and motivating atmosphere that is designed for athletes, young and old.</p>
  <span class="field-label" style="top:206px">Email / Username</span>
  <svg class="abs" style="left:232px;top:205px" width="14" height="11" viewBox="0 0 14 11"><path d="M1 6l4 4 8-9" stroke="#4fd6b0" stroke-width="1.6" fill="none"/></svg>
  <div class="field-line" style="top:224px"></div>
  <span class="field-label" style="top:244px">Password</span>
  <span class="abs" style="right:32px;top:244px;font-size:9px;color:var(--coral)">Forgot?</span>
  <div class="field-line" style="top:262px"></div>
  <div class="btn-login">Login</div>
  <p class="abs" style="left:0;right:0;top:373px;text-align:center;font-size:8.5px;color:#d0d2d4">Don't have a account? <b style="color:var(--coral)">SignUp</b></p>
</section>

<!-- 3 dashboard -->
<section class="phone" style="left:611px;top:171px">
  <div class="status"><span>●●○○○ Carrierly</span><span>14:39</span><span class="batt"></span></div>
  <div class="hero">
    <span class="abs" style="left:16px;top:18px;width:44px;height:44px;border-radius:50%;background:var(--yellow);border:2px solid #fff"></span>
    <span class="abs" style="left:70px;top:23px;font-size:10.5px">FC Brookvale – Juniors</span>
    <span class="abs" style="left:70px;top:42px;font-size:9px;color:#d4d6d8">⌾ Riverton, USA</span>
    <svg class="abs" style="left:251px;top:14px" width="16" height="16" viewBox="0 0 16 16"><circle cx="8" cy="8" r="5" stroke="#fff" stroke-width="1.4" fill="none" stroke-dasharray="2.2 1.3"/><circle cx="8" cy="8" r="2" stroke="#fff" stroke-width="1.2" fill="none"/></svg>
    <span class="abs" style="right:34px;top:56px;font-size:21px;font-weight:500">30°</span>
    <div class="datecard"><div class="m">APR</div><div class="d">26</div></div>
    <span class="abs" style="left:23px;top:125px;font-size:10px">17:30</span>
    <span class="abs" style="left:82px;top:80px;width:1px;height:60px;background:#44474a"></span>
    <svg class="abs" style="left:104px;top:84px" width="40" height="32" viewBox="0 0 40 32"><g stroke="#fff" stroke-width="1.6" fill="none"><circle cx="24" cy="12" r="6"/><path d="M24 1v3M33 12h3M31 5l2-2M17 5l-2-2"/><path d="M8 28h20a6 6 0 0 0 0-12 8 8 0 0 0-15 2 5 5 0 0 0-5 10z" fill="#25282b"/></g></svg>
    <span class="abs" style="left:106px;top:125px;font-size:9.5px;color:#d4d6d8">Cloudy</span>
    <div class="wx"><span>Feel like</span><span>38°</span><span>Humidity</span><span>63%</span><span>Pressure</span><span>30.10 in</span><span style="color:var(--muted)">Precipitation</span><span style="color:var(--muted)">0% in</span></div>
  </div>
  <div class="bigbtn"></div>
  <svg class="abs" style="left:209px;top:178px" width="20" height="20" viewBox="0 0 20 20"><path d="M16 8a6.5 6.5 0 1 0 .5 4M16 3v5h-5" stroke="#555" stroke-width="1.8" fill="none"/></svg>
  <span class="section-title" style="top:307px">Elements</span>
  <div class="row" style="top:325px"><span class="flag" style="background:var(--sky)"></span><span class="name">WARM-UP</span><span class="pill" style="background:var(--sky)">20 min</span></div>
  <div class="row" style="top:350px"><span class="flag" style="background:var(--sky)"></span><span class="name">4 Vs. 2</span><span class="pill" style="background:var(--sky)">25 min</span></div>
  <div class="row" style="top:375px"><span class="flag" style="background:var(--sky)"></span><span class="name">Offensive 2 vs. 1</span><span class="pill" style="background:var(--sky)">20 min</span></div>
  <div class="row" style="top:400px"><span class="flag" style="background:var(--sky)"></span><span class="name">Game 7 on 7</span><span class="pill" style="background:var(--sky)">25 min</span></div>
  <svg class="abs" style="left:246px;top:327px" width="16" height="94" viewBox="0 0 16 94"><g stroke="#9a9da0" stroke-width="1.4" fill="none"><path id="rf" d="M13 6a5.5 5.5 0 1 0 .4 4M13 2v4h-4"/><use href="#rf" y="25"/><use href="#rf" y="50"/><use href="#rf" y="75"/></g></svg>
  <div class="link-row" style="top:432px">Trained Skills<i class="chev" style="right:12px"></i></div>
  <div class="link-row" style="top:459px;border:0">Prerequisites<i class="chev" style="right:12px"></i></div>
</section>

<!-- 4 session -->
<section class="phone" style="left:904px;top:171px;background:var(--light-b)">
  <div class="status"><span>●●○○○ Carrierly</span><span>14:39</span><span class="batt"></span></div>
  <header class="topbar"><i class="back"></i>14 Apr 2016, 15:24 hr</header>
  <span class="section-title" style="top:71px">Elements</span>
  <div class="row" style="top:89px"><span class="flag" style="background:var(--teal)"></span><span class="name">WARM-UP</span><span class="pill" style="background:var(--teal)"><svg width="12" height="9" viewBox="0 0 12 9"><path d="M1 4.5l3.5 3.5 6.5-7" stroke="#fff" stroke-width="1.5" fill="none"/></svg></span><i class="chev"></i></div>
  <div class="row" style="top:114px"><span class="flag" style="background:var(--coral)"></span><span class="name">4 Vs. 2</span><span class="pill" style="background:var(--coral)">4.5 min</span><i class="chev"></i></div>
  <div class="row" style="top:138px"><span class="flag" style="background:var(--teal)"></span><span class="name">Offensive 2 vs. 1</span><span class="pill" style="background:var(--teal)">11 min</span><i class="chev"></i></div>
  <div class="row" style="top:163px"><span class="flag" style="background:var(--sky)"></span><span class="name">Game 7 on 7</span><span class="pill" style="background:var(--sky)">25 min</span><i class="chev"></i></div>
  <div class="band" style="top:202px">Offensive 2 vs. 1</div>
  <div class="pitch" style="left:18px;top:232px;width:244px;height:152px" role="img" aria-label="Play diagram on a green pitch: player markers, cones and run lines"></div>
  <span class="abs" style="left:0;right:0;top:233px;text-align:center;font-size:10px;font-weight:700;color:#1c1e20">Spin 3MO 45 FB Dive</span>
  <p class="para" style="left:18px;right:18px;top:395px;height:61px;overflow:hidden">Lorem Ipsum is simply dummy text of the printing and typesetting industry. Lorem Ipsum has been the industry's standard dummy text ever since the 1500s, when an unknown printer took a galley of type and scrambled it to make a type specimen book. It has survived not only five centuries, but also</p>
  <div class="finish">FINISH TRAINING</div>
</section>

<!-- 5 drill info -->
<section class="phone" style="left:24px;top:698px">
  <div class="status"><span>●●○○○ Carrierly</span><span>14:39</span><span class="batt"></span></div>
  <header class="topbar"><i class="back"></i>Offensive 2 vs. 1</header>
  <div class="pitch" style="left:18px;top:52px;width:244px;height:101px" role="img" aria-label="Play diagram on a green pitch: player markers, cones and run lines"></div>
  <span class="slider-label" style="left:18px;top:163px">Strength</span>
  <div class="abs" style="left:18px;top:178px;font-size:8.6px;line-height:12.8px;display:grid;grid-template-columns:92px auto;column-gap:5px">
    <b style="text-align:right">Speed Warm-up :</b><span>45-60 min</span>
    <b style="text-align:right">Snatch :</b><span>3 x (3-4) x 30% – 50%</span>
    <b style="text-align:right">sqaut :</b><span>4-5 x (1-10) x 60% – 100%</span>
    <b style="text-align:right">RDL :</b><span>3 x 5 x 50% – 65%</span>
  </div>
  <p class="para" style="left:12px;right:12px;top:235px">My Ridgeline Hawk team ran this play to perfection with two big fullbacks rotating in to keep them fresh for blocking and running this play all over our opponent's defenses. Depending of the defensive alignments of the defenses d-tackles you either run to the 5 or 3 holes for a nice gainer from your fullbacks. You can also run the play from Double Tights or a traditional Spread. I personally like to run it from the Nasty Spread as shown below. The play is set up by the Spin Sweeps, Counters and Reverses. You want to lull the defense to sleep then hit them with a quick FB dive.</p>
  <span class="slider-label" style="left:18px;top:368px">Video</span>
  <div class="abs" style="left:18px;top:385px;width:244px;height:70px;background:linear-gradient(160deg,#5a8d4e,#3d6b39)" role="img" aria-label="Video still of a soccer match with a play button"></div>
  <nav class="tabbar">
    <div class="tab on"><svg width="26" height="20" viewBox="0 0 26 20"><rect x="2" y="4" width="18" height="14"/><path d="M6 2h18v13"/><path d="M9 8l6 3-6 3z"/></svg>Info</div>
    <div class="tab"><svg width="26" height="20" viewBox="0 0 26 20"><path d="M4 6h18M4 11h18M4 16h18"/></svg>Skills</div>
    <div class="tab"><svg width="26" height="20" viewBox="0 0 26 20"><circle cx="11" cy="9" r="6"/><path d="M15.5 13.5l5 5"/></svg>Prerequisites</div>
  </nav>
</section>

<!-- 6 skills (read) -->
<section class="phone" style="left:318px;top:698px">
  <div class="status"><span>●●○○○ Carrierly</span><span>14:39</span><span class="batt"></span></div>
  <header class="topbar"><i class="back"></i>Offensive 2 vs. 1</header>
  <p class="para" style="left:18px;right:18px;top:72px;height:33px;overflow:hidden">Lorem Ipsum is simply dummy text of the printing and typesetting industry. Lorem Ipsum has been the industry's standard dummy text ever since the</p>
  <span class="slider-label" style="top:130px">Coordination</span><span class="scale" style="left:17px;top:150px">0</span><div class="track" style="top:153px"><div class="fill coral" style="width:35%"></div></div><span class="scale" style="left:254px;top:150px">100</span>
  <span class="slider-label" style="top:179px">Finishing</span><span class="scale" style="left:17px;top:199px">0</span><div class="track" style="top:202px"><div class="fill coral" style="width:75%"></div></div><span class="scale" style="left:254px;top:199px">100</span>
  <span class="slider-label" style="top:228px">Stamina</span><span class="scale" style="left:17px;top:248px">0</span><div class="track" style="top:251px"><div class="fill coral" style="width:66%"></div></div><span class="scale" style="left:254px;top:248px">100</span>
  <span class="slider-label" style="top:277px">Speed</span><span class="scale" style="left:17px;top:297px">0</span><div class="track" style="top:300px"><div class="fill teal" style="width:90%"></div></div><span class="scale" style="left:254px;top:297px">100</span>
  <span class="slider-label" style="top:326px">Understanding of Game</span><span class="scale" style="left:17px;top:346px">0</span><div class="track" style="top:349px"><div class="fill coral" style="width:66%"></div></div><span class="scale" style="left:254px;top:346px">100</span>
  <span class="slider-label" style="top:375px">Devensive Behavior</span><span class="scale" style="left:17px;top:395px">0</span><div class="track" style="top:398px"><div class="fill teal" style="width:90%"></div></div><span class="scale" style="left:254px;top:395px">100</span>
  <nav class="tabbar">
    <div class="tab"><svg width="26" height="20" viewBox="0 0 26 20"><rect x="2" y="4" width="18" height="14"/><path d="M6 2h18v13"/><path d="M9 8l6 3-6 3z"/></svg>Info</div>
    <div class="tab on"><svg width="26" height="20" viewBox="0 0 26 20"><path d="M4 6h18M4 11h18M4 16h18"/></svg>Skills</div>
    <div class="tab"><svg width="26" height="20" viewBox="0 0 26 20"><circle cx="11" cy="9" r="6"/><path d="M15.5 13.5l5 5"/></svg>Prerequisites</div>
  </nav>
</section>

<!-- 7 prerequisites (read) -->
<section class="phone" style="left:611px;top:698px">
  <div class="status"><span>●●○○○ Carrierly</span><span>14:39</span><span class="batt"></span></div>
  <header class="topbar"><i class="back"></i>Offensive 2 vs. 1</header>
  <div class="kit" style="top:71px">Cones<span class="qty">20</span></div>
  <div class="kit" style="top:105px">Goals<span class="qty">4</span></div>
  <div class="kit" style="top:139px">Players<span class="qty">18</span></div>
  <div class="kit" style="top:174px">Goalies<span class="qty">6</span></div>
  <nav class="tabbar">
    <div class="tab"><svg width="26" height="20" viewBox="0 0 26 20"><rect x="2" y="4" width="18" height="14"/><path d="M6 2h18v13"/><path d="M9 8l6 3-6 3z"/></svg>Info</div>
    <div class="tab"><svg width="26" height="20" viewBox="0 0 26 20"><path d="M4 6h18M4 11h18M4 16h18"/></svg>Skills</div>
    <div class="tab on"><svg width="26" height="20" viewBox="0 0 26 20"><circle cx="11" cy="9" r="6"/><path d="M15.5 13.5l5 5"/></svg>Prerequisites</div>
  </nav>
</section>

<!-- 8 trained skills (edit) -->
<section class="phone" style="left:904px;top:698px">
  <div class="status"><span>●●○○○ Carrierly</span><span>14:39</span><span class="batt"></span></div>
  <header class="topbar"><i class="back"></i>Trained Skills</header>
  <p class="para" style="left:18px;right:18px;top:72px;height:33px;overflow:hidden">Lorem Ipsum is simply dummy text of the printing and typesetting industry. Lorem Ipsum has been the industry's standard dummy text ever since the</p>
  <span class="slider-label" style="top:130px">Coordination</span><span class="scale" style="left:17px;top:150px">0</span><div class="track" style="top:153px"><div class="fill coral" style="width:33%"></div><span class="knob" style="left:33%"></span></div><span class="scale" style="left:254px;top:150px">100</span>
  <span class="slider-label" style="top:179px">Finishing</span><span class="scale" style="left:17px;top:199px">0</span><div class="track" style="top:202px"><div class="fill coral" style="width:73%"></div><span class="knob" style="left:73%"></span></div><span class="scale" style="left:254px;top:199px">100</span>
  <span class="slider-label" style="top:228px">Stamina</span><span class="scale" style="left:17px;top:248px">0</span><div class="track" style="top:251px"><div class="fill coral" style="width:64%"></div><span class="knob" style="left:64%"></span></div><span class="scale" style="left:254px;top:248px">100</span>
  <span class="slider-label" style="top:277px">Speed</span><span class="scale" style="left:17px;top:297px">0</span><div class="track" style="top:300px"><div class="fill teal" style="width:88%"></div><span class="knob" style="left:88%"></span></div><span class="scale" style="left:254px;top:297px">100</span>
  <span class="slider-label" style="top:326px">Understanding of Game</span><span class="scale" style="left:17px;top:346px">0</span><div class="track" style="top:349px"><div class="fill coral" style="width:65%"></div><span class="knob" style="left:65%"></span></div><span class="scale" style="left:254px;top:346px">100</span>
  <span class="slider-label" style="top:375px">Devensive Behavior</span><span class="scale" style="left:17px;top:395px">0</span><div class="track" style="top:398px"><div class="fill teal" style="width:88%"></div><span class="knob" style="left:88%"></span></div><span class="scale" style="left:254px;top:395px">100</span>
</section>

<!-- 9 prerequisites (edit) -->
<section class="phone" style="left:1197px;top:698px">
  <div class="status"><span>●●○○○ Carrierly</span><span>14:39</span><span class="batt"></span></div>
  <header class="topbar"><i class="back"></i>Offensive 2 vs. 1</header>
  <div class="kit" style="top:71px">Cones<span class="stepper"><span class="step">«</span><span class="qty">20</span><span class="step on">»</span></span></div>
  <div class="kit" style="top:105px">Goals<span class="stepper"><span class="step">«</span><span class="qty">4</span><span class="step">»</span></span></div>
  <div class="kit" style="top:139px">Players<span class="stepper"><span class="step">«</span><span class="qty">18</span><span class="step">»</span></span></div>
  <div class="kit" style="top:174px">Goalies<span class="stepper"><span class="step">«</span><span class="qty">6</span><span class="step">»</span></span></div>
</section>

</main>
</body>
</html>
```